PowerPoint Template Design for Quarry Lending

Design a PowerPoint template for Quarry Lending, tailored for presentations to sophisticated mortgage servicing investors. The template should reflect a high level of professionalism, with a clean and modern aesthetic that resonates with an informed and discerning audience. The design must effectively integrate Quarry Lending's branding elements, ensuring a coherent visual narrative that reinforces our reputation for expertise and reliability in the mortgage servicing sector.

```html
<!DOCTYPE html>
<html lang="en">
<head>
<meta charset="utf-8">
<title>Quarry Lending Presentation Template</title>
<link rel="stylesheet" href="https://fonts.googleapis.com/css2?family=Poppins:wght@400;500;600;700;800&display=swap">
<style>
:root{
  --navy:#221d5e;
  --navy-deep:#15123f;
  --gold:#d4a431;
  --gold-soft:#e3bb4c;
  --band:#e4e4e6;
  --paper:#ffffff;
  --ink:#2a2740;
  --stage:#c9cccd;
}
*{box-sizing:border-box;margin:0;padding:0}
html,body{width:874px;height:1200px;overflow:hidden;background:var(--stage);font-family:'Poppins',sans-serif;color:var(--ink)}
.deck{position:relative;width:874px;height:1200px}
.slide{position:absolute;width:411px;height:231px;background:var(--paper);overflow:hidden;box-shadow:0 8px 14px rgba(0,0,0,.18)}
.slide *{position:absolute}
.slide svg{overflow:visible}
.col-a{left:22px}.col-b{left:441px}
.row-1{top:230px}.row-2{top:485px}.row-3{top:740px}
.title{font-weight:800;color:var(--navy);line-height:1.05;letter-spacing:-.2px;white-space:nowrap}
.body{font-size:4.3px;line-height:1.5;color:var(--ink)}
.head{font-size:6.2px;font-weight:600;color:var(--navy);white-space:nowrap}
.rule{height:1.3px;background:var(--gold)}
.brand{font-weight:700;color:var(--gold);white-space:nowrap}
.photo{position:absolute}
.tick-list{display:block}
.tick-list li{position:relative;list-style:none;font-size:4.6px;line-height:1.25;height:17.5px;padding-left:8px;color:var(--ink)}
.tick-list li::before{content:"";position:absolute;left:0;top:1px;width:3.2px;height:3.2px;border:.8px solid var(--navy);border-radius:50%}
</style>
</head>
<body>
<main class="deck">

  <!-- Slide 1: cover -->
  <section class="slide col-a row-1">
    <svg class="photo" role="img" aria-label="Photo of a family walking toward a blue two-storey house" width="411" height="231" viewBox="0 0 411 231">
      <defs>
        <linearGradient id="houseSky" x1="0" y1="0" x2="0" y2="1">
          <stop offset="0" stop-color="#c9cde3"/><stop offset=".5" stop-color="#5f6f8e"/><stop offset=".8" stop-color="#4b5e53"/><stop offset="1" stop-color="#7a9a45"/>
        </linearGradient>
      </defs>
      <path d="M120 0H411V206Q330 236 262 222Q182 200 164 130Q150 60 120 0Z" fill="url(#houseSky)"/>
    </svg>
    <div class="brand" style="left:244px;top:22px;font-size:17px">Quarry Lending</div>
    <div class="title" style="left:16px;top:18px;font-size:16px">YOUR <span style="position:relative;display:inline-block;width:26px;height:1.4px;background:var(--navy);vertical-align:middle"></span></div>
    <div class="title" style="left:16px;top:39px;font-size:16px">TITLE HERE</div>
    <p class="body" style="left:16px;top:64px;width:102px">Lorem ipsum dolor sit amet, consectetur adipiscing elit, sed do eiusmod tempor incididunt ut labore et dolore magna aliqua. Quis ipsum suspendisse ultrices gravida. Risus commodo viverra maecenas.</p>
    <p class="body" style="left:16px;top:100px;width:102px">Lorem ipsum dolor sit amet, consectetur adipiscing elit, sed do eiusmod.</p>
    <svg width="411" height="231" viewBox="0 0 411 231" style="left:0;top:0"><path d="M0 126H165Q172 145 180 160H0Z" fill="var(--band)"/></svg>
    <div class="brand" style="left:16px;top:135px;font-size:9px">Quarry Lending</div>
    <div class="brand" style="left:86px;top:137px;font-size:6.6px;font-weight:600">CONTACT DETAILS</div>
    <svg width="14" height="22" viewBox="0 0 14 22" style="left:15px;top:174px">
      <rect x="1" y="1" width="10" height="18" rx="2" fill="none" stroke="var(--navy)" stroke-width="1.6"/>
      <circle cx="6" cy="15" r="1.3" fill="var(--navy)"/>
      <path d="M12.5 7q1.5 2 0 4" fill="none" stroke="var(--navy)" stroke-width=".9"/>
    </svg>
    <div style="left:41px;top:173px;font-size:7px;color:var(--navy);white-space:nowrap">MORE INFORMATION CALL US</div>
    <div style="left:41px;top:183px;font-size:10px;font-weight:700;color:var(--navy);letter-spacing:1px;white-space:nowrap">+1-555-014-2778</div>
    <svg width="6" height="9" viewBox="0 0 6 9" style="left:15px;top:210px"><path d="M3 8.5C1 5.8.5 4.5.5 3.3a2.5 2.5 0 015 0c0 1.2-.5 2.5-2.5 5.2z" fill="none" stroke="var(--navy)" stroke-width=".8"/><circle cx="3" cy="3.2" r=".9" fill="var(--navy)"/></svg>
    <div style="left:25px;top:209px;font-size:4.3px;line-height:1.3;color:var(--navy)">Av. Lorem ipsum dolor 2045<br>Dolor sit Amet - Adress</div>
    <svg width="8" height="8" viewBox="0 0 8 8" style="left:99px;top:211px"><circle cx="4" cy="4" r="3.4" fill="none" stroke="var(--navy)" stroke-width=".7"/><ellipse cx="4" cy="4" rx="1.5" ry="3.4" fill="none" stroke="var(--navy)" stroke-width=".6"/><path d="M.6 4h6.8" stroke="var(--navy)" stroke-width=".6"/></svg>
    <div style="left:112px;top:212px;font-size:4.6px;font-weight:600;letter-spacing:.4px;color:var(--navy);white-space:nowrap">WWW.QUARRYLENDING.NET</div>
  </section>

  <!-- Slide 2: infographic -->
  <section class="slide col-b row-1">
    <div class="title" style="left:20px;top:14px;font-size:14.5px">YOUR INFOGRAPHIC</div>
    <div class="title" style="left:20px;top:35px;font-size:14.5px">PAGE TITTLE</div>
    <div class="rule" style="left:134px;top:43px;width:62px"></div>

    <div class="head" style="left:20px;top:69px">YOUR HEADING</div>
    <ul class="tick-list" style="left:20px;top:83px;width:60px"><li>Lorem ipsum dolor sit amet.</li><li>Lorem ipsum dolor sit amet.</li><li>Lorem ipsum dolor sit amet.</li></ul>
    <div class="head" style="left:150px;top:69px">YOUR HEADING</div>
    <ul class="tick-list" style="left:150px;top:83px;width:60px"><li>Lorem ipsum dolor sit amet.</li><li>Lorem ipsum dolor sit amet.</li><li>Lorem ipsum dolor sit amet.</li></ul>
    <div class="head" style="left:20px;top:150px">YOUR HEADING</div>
    <ul class="tick-list" style="left:20px;top:165px;width:60px"><li>Lorem ipsum dolor sit amet.</li><li>Lorem ipsum dolor sit amet.</li><li>Lorem ipsum dolor sit amet.</li></ul>
    <div class="head" style="left:150px;top:150px">YOUR HEADING</div>
    <ul class="tick-list" style="left:150px;top:165px;width:60px"><li>Lorem ipsum dolor sit amet.</li><li>Lorem ipsum dolor sit amet.</li><li>Lorem ipsum dolor sit amet.</li></ul>

    <svg width="411" height="231" viewBox="0 0 411 231" style="left:0;top:0">
      <g fill="none" stroke="var(--navy)" stroke-width=".5">
        <path d="M84 73H102V110"/><path d="M146 73H129V100"/><path d="M52 153V146H98V152"/><path d="M150 153V146H128V158"/>
      </g>
      <circle cx="84" cy="73" r="1.4" fill="#fff" stroke="var(--navy)" stroke-width=".6"/>
      <circle cx="146" cy="73" r="1.4" fill="#fff" stroke="var(--navy)" stroke-width=".6"/>
      <!-- bars -->
      <path d="M92 116l10-6 10 6V231H92Z" fill="var(--navy)"/>
      <path d="M118 104l10-6 10 6V231H118Z" fill="var(--gold)"/>
      <path d="M86 158l10-6 10 6V231H86Z" fill="var(--gold)"/>
      <path d="M112 163l10-6 10 6V231H112Z" fill="var(--navy)"/>
      <g fill="#fff"><circle cx="102" cy="118" r="2.5"/><circle cx="128" cy="106" r="2.5"/><circle cx="96" cy="160" r="2.5"/><circle cx="122" cy="165" r="2.5"/></g>
      <defs><linearGradient id="city" x1="0" y1="0" x2="0" y2="1"><stop offset="0" stop-color="#a9c7e6"/><stop offset=".45" stop-color="#c5b9a6"/><stop offset=".7" stop-color="#5d7a4c"/><stop offset="1" stop-color="#3c5a2b"/></linearGradient></defs>
    </svg>
    <svg class="photo" role="img" aria-label="Photo of a waterfront city skyline with palm trees" width="190" height="231" viewBox="0 0 190 231" style="left:221px;top:0">
      <path d="M0 41L70 0H190V231H3Z" fill="url(#city)"/>
      <g fill="none" stroke="var(--gold-soft)" stroke-width="1.6">
        <path d="M0 41L70 0 138 41V124L70 164 3 124V41"/>
        <path d="M138 41L190 11"/><path d="M138 124L190 154"/><path d="M70 164V231"/><path d="M3 124V231"/><path d="M138 124V231"/>
      </g>
    </svg>
  </section>

  <!-- Slide 3: circle list -->
  <section class="slide col-a row-2">
    <svg class="photo" role="img" aria-label="Photo of a bright interior room with wooden floor" width="175" height="231" viewBox="0 0 175 231" style="left:-4px;top:0">
      <defs><linearGradient id="room" x1="0" y1="0" x2="1" y2="1"><stop offset="0" stop-color="#d8d8d8"/><stop offset=".6" stop-color="#a9a9a6"/><stop offset="1" stop-color="#6b4b34"/></linearGradient></defs>
      <rect width="175" height="231" fill="url(#room)"/>
    </svg>
    <svg width="175" height="231" viewBox="0 0 175 231" style="left:0;top:0">
      <circle cx="0" cy="115" r="154" fill="none" stroke="var(--gold)" stroke-width="1.4"/>
      <path d="M0 -38A153 153 0 0 1 0 268Z" fill="var(--navy)"/>
      <path d="M0 -38A153 153 0 0 1 85 -12L0 115Z" fill="#b3b3b3"/>
      <path d="M0 -38A153 153 0 0 1 85 -12L0 115Z" fill="#c9c9c9" opacity=".6"/>
      <g stroke="#2d2872" stroke-width=".8"><path d="M0 115L140 54"/><path d="M0 115L140 176"/><path d="M0 115L85 242"/></g>
      <circle cx="0" cy="115" r="66" fill="#fff" stroke="#d0d0d0" stroke-width="4"/>
      <g fill="none" stroke="#fff" stroke-width="1.1">
        <path d="M18 35q-6 4-6 10h12q0-6-6-10z"/><path d="M66 58v8M72 53v13M78 50v16M62 66h20"/>
        <circle cx="93" cy="116" r="6"/><circle cx="93" cy="116" r="3"/><path d="M93 116l8-8"/>
        <ellipse cx="72" cy="173" rx="5" ry="2"/><path d="M67 173v8q5 3 10 0v-8"/>
        <circle cx="13" cy="194" r="2.5"/><circle cx="22" cy="194" r="2.5"/><path d="M8 203q5-6 10 0M17 203q5-6 10 0"/>
      </g>
    </svg>
    <div class="brand" style="left:6px;top:109px;font-size:8.5px">Quarry Lending</div>
    <div class="title" style="left:173px;top:13px;font-size:14.5px">YOUR PAGE TITTLE</div>
    <div class="rule" style="left:173px;top:34px;width:127px"></div>
    <svg width="22" height="180" viewBox="0 0 22 180" style="left:172px;top:48px" fill="none" stroke="var(--navy)" stroke-width=".8">
      <path d="M10 2q-6 4-6 11h12q0-7-6-11z"/>
      <path d="M5 42v6M9 38v10M13 35v13M3 48h13"/>
      <circle cx="10" cy="76" r="6"/><circle cx="10" cy="76" r="2.5"/><path d="M10 76l7-7"/>
      <ellipse cx="10" cy="104" rx="5" ry="2"/><path d="M5 104v7q5 3 10 0v-7"/>
      <circle cx="6" cy="134" r="2.3"/><circle cx="14" cy="134" r="2.3"/><path d="M2 142q4-5 8 0M10 142q4-5 8 0"/>
    </svg>
    <div style="left:198px;top:47px;width:200px">
      <div class="head" style="position:relative;font-weight:500">TITLE : 1</div>
      <p class="body" style="position:relative;margin-bottom:10px">Lorem ipsum dolor sit amet, consectetur adipiscing elit, sed do eiusmod tempor incididunt ut labore et dolore magna aliqua. Quis ipsum .</p>
      <div class="head" style="position:relative;font-weight:500">TITLE : 2</div>
      <p class="body" style="position:relative;margin-bottom:10px">Lorem ipsum dolor sit amet, consectetur adipiscing elit, sed do eiusmod tempor incididunt ut labore et dolore magna aliqua. Quis ipsum .</p>
      <div class="head" style="position:relative;font-weight:500">TITLE : 3</div>
      <p class="body" style="position:relative;margin-bottom:10px">Lorem ipsum dolor sit amet, consectetur adipiscing elit, sed do eiusmod tempor incididunt ut labore et dolore magna aliqua. Quis ipsum .</p>
      <div class="head" style="position:relative;font-weight:500">TITLE : 4</div>
      <p class="body" style="position:relative;margin-bottom:10px">Lorem ipsum dolor sit amet, consectetur adipiscing elit, sed do eiusmod tempor incididunt ut labore et dolore magna aliqua. Quis ipsum .</p>
      <div class="head" style="position:relative;font-weight:500">TITLE : 5</div>
      <p class="body" style="position:relative">Lorem ipsum dolor sit amet, consectetur adipiscing elit, sed do eiusmod tempor incididunt ut labore et dolore magna aliqua. Quis ipsum .</p>
    </div>
  </section>

  <!-- Slide 4: gallery -->
  <section class="slide col-b row-2">
    <div class="title" style="left:19px;top:17px;font-size:13px">YOUR PAGE TITTLE</div>
    <p class="body" style="left:23px;top:44px;width:190px;text-align:justify">Lorem ipsum dolor sit amet, consectetur adipiscing elit, sed do eiusmod tempor incididunt ut labore et dolore magna aliqua. Quis ipsum suspendisse ultrices gravida. Risus commodo viverra maecenas accumsan lacus vel facilisis. Lorem ipsum dolor sit amet, consectetur adipiscing elit, sed do eiusmod tempor incididunt ut labore et dolore magna aliqua. Quis ipsum suspendisse ultrices gravida. Risus commodo viverra maecenas accumsan lacus vel facilisis. Lorem ipsum dolor sit amet, consectetur adipiscing elit, sed do eiusmod.</p>
    <svg width="180" height="100" viewBox="0 0 180 100" style="left:40px;top:113px" fill="none" stroke="var(--gold)" stroke-width="1.3">
      <g id="handHouse"><path d="M0 6l5-4 5 4v4H0z"/><path d="M-3 10q8 5 16 0"/></g>
      <use href="#handHouse" x="104"/><use href="#handHouse" y="56"/><use href="#handHouse" x="104" y="56"/>
    </svg>
    <div style="left:25px;top:127px;width:75px;text-align:center">
      <div class="head" style="position:relative;font-size:4.8px;font-weight:700">LOREM IPSUM</div>
      <p class="body" style="position:relative;margin-top:4px">Lorem ipsum dolor sit amet, consectetur adipiscing elit sed do eiusmod tempor.</p>
    </div>
    <div style="left:129px;top:127px;width:75px;text-align:center">
      <div class="head" style="position:relative;font-size:4.8px;font-weight:700">LOREM IPSUM</div>
      <p class="body" style="position:relative;margin-top:4px">Lorem ipsum dolor sit amet, consectetur adipiscing elit sed do eiusmod tempor.</p>
    </div>
    <div style="left:25px;top:183px;width:75px;text-align:center">
      <div class="head" style="position:relative;font-size:4.8px;font-weight:700">LOREM IPSUM</div>
      <p class="body" style="position:relative;margin-top:4px">Lorem ipsum dolor sit amet, consectetur adipiscing elit sed do eiusmod tempor.</p>
    </div>
    <div style="left:129px;top:183px;width:75px;text-align:center">
      <div class="head" style="position:relative;font-size:4.8px;font-weight:700">LOREM IPSUM</div>
      <p class="body" style="position:relative;margin-top:4px">Lorem ipsum dolor sit amet, consectetur adipiscing elit sed do eiusmod tempor.</p>
    </div>

    <div class="title" style="left:235px;top:19px;font-size:11px">01</div>
    <div class="title" style="left:322px;top:19px;font-size:11px">03</div>
    <div class="title" style="left:234px;top:124px;font-size:11px">02</div>
    <div class="title" style="left:321px;top:124px;font-size:11px">04</div>
    <div class="photo" role="img" aria-label="Photo of a tower among palm trees" style="left:253px;top:20px;width:57px;height:68px;background:linear-gradient(180deg,#9cc0e3,#c9b69a 55%,#4e6a39)"></div>
    <div class="photo" role="img" aria-label="Photo of a city skyline over a harbour" style="left:341px;top:20px;width:57px;height:68px;background:linear-gradient(180deg,#a7c9ea,#b9b9b3 55%,#3f79a3)"></div>
    <div class="photo" role="img" aria-label="Photo of a marina with city towers" style="left:253px;top:125px;width:57px;height:68px;background:linear-gradient(180deg,#a7c9ea,#c3b7a1 50%,#3b6f95)"></div>
    <div class="photo" role="img" aria-label="Photo of waterfront towers and trees" style="left:341px;top:125px;width:57px;height:68px;background:linear-gradient(180deg,#a7c9ea,#bdb7a6 50%,#3a6d8e)"></div>
    <div style="left:253px;top:92px;width:60px"><div class="head" style="position:relative;font-size:4.3px;font-weight:700">Place Name Here</div><p class="body" style="position:relative;font-size:3px;line-height:1.35;margin-top:2px">Lorem ipsum dolor sit amet, consectetur adipiscing elit, sed do eiusmod tempor incididunt ut labore et dolore magna aliqua.</p></div>
    <div style="left:341px;top:92px;width:60px"><div class="head" style="position:relative;font-size:4.3px;font-weight:700">Place Name Here</div><p class="body" style="position:relative;font-size:3px;line-height:1.35;margin-top:2px">Lorem ipsum dolor sit amet, consectetur adipiscing elit, sed do eiusmod tempor incididunt ut labore et dolore magna aliqua.</p></div>
    <div style="left:253px;top:197px;width:60px"><div class="head" style="position:relative;font-size:4.3px;font-weight:700">Place Name Here</div><p class="body" style="position:relative;font-size:3px;line-height:1.35;margin-top:2px">Lorem ipsum dolor sit amet, consectetur adipiscing elit, sed do eiusmod tempor incididunt ut labore et dolore magna aliqua.</p></div>
    <div style="left:341px;top:197px;width:60px"><div class="head" style="position:relative;font-size:4.3px;font-weight:700">Place Name Here</div><p class="body" style="position:relative;font-size:3px;line-height:1.35;margin-top:2px">Lorem ipsum dolor sit amet, consectetur adipiscing elit, sed do eiusmod tempor incididunt ut labore et dolore magna aliqua.</p></div>
  </section>

  <!-- Slide 5: headings list -->
  <section class="slide col-a row-3">
    <svg class="photo" role="img" aria-label="Illustration of hands holding a glowing house outline over finance charts" width="200" height="231" viewBox="0 0 200 231" style="left:0;top:0">
      <defs><radialGradient id="digital" cx=".4" cy=".55" r=".7"><stop offset="0" stop-color="#3a5e9a"/><stop offset=".6" stop-color="#173a73"/><stop offset="1" stop-color="#0b1f4a"/></radialGradient></defs>
      <path d="M0 0H171Q205 115 168 231H0Z" fill="url(#digital)"/>
      <path d="M171 0Q205 115 168 231" fill="none" stroke="var(--gold)" stroke-width="1.6"/>
    </svg>
    <div class="title" style="right:24px;top:9px;font-size:25px;text-align:right">YOUR PAGE</div>
    <div class="title" style="right:24px;top:37px;font-size:25px;text-align:right">TITTLE</div>
    <div class="rule" style="left:231px;top:53px;width:63px"></div>
    <div style="left:200px;top:76px;width:151px;text-align:right">
      <div class="head" style="position:relative;font-size:5.6px;font-weight:700">YOUR HEADING</div>
      <p class="body" style="position:relative;margin:2px 0 12px">Lorem ipsum dolor sit amet, consectetur adipiscing elit, sed do eiusmod tempor incididunt ut labore et dolore magna</p>
      <div class="head" style="position:relative;font-size:5.6px;font-weight:700">YOUR HEADING</div>
      <p class="body" style="position:relative;margin:2px 0 12px">Lorem ipsum dolor sit amet, consectetur adipiscing elit, sed do eiusmod tempor incididunt ut labore et dolore magna</p>
      <div class="head" style="position:relative;font-size:5.6px;font-weight:700">YOUR HEADING</div>
      <p class="body" style="position:relative;margin:2px 0 12px">Lorem ipsum dolor sit amet, consectetur adipiscing elit, sed do eiusmod tempor incididunt ut labore et dolore magna</p>
      <div class="head" style="position:relative;font-size:5.6px;font-weight:700">YOUR HEADING</div>
      <p class="body" style="position:relative;margin-top:2px">Lorem ipsum dolor sit amet, consectetur adipiscing elit, sed do eiusmod tempor incididunt ut labore et dolore magna</p>
    </div>
    <svg width="18" height="120" viewBox="0 0 18 120" style="left:363px;top:81px">
      <g id="houseBadge"><rect width="17" height="17" rx="3" fill="var(--navy)"/><path d="M4 8.5l4.5-4 4.5 4v4H4z" fill="none" stroke="var(--gold)" stroke-width="1.1"/></g>
      <use href="#houseBadge" y="34"/><use href="#houseBadge" y="68"/><use href="#houseBadge" y="102"/>
    </svg>
  </section>

  <!-- Slide 6: diagonal sub-headings -->
  <section class="slide col-b row-3">
    <svg class="photo" role="img" aria-label="Photo of a high-rise tower behind palm trees" width="230" height="231" viewBox="0 0 230 231" style="left:0;top:0">
      <defs><linearGradient id="tower" x1="0" y1="0" x2=".6" y2="1"><stop offset="0" stop-color="#a9c8e8"/><stop offset=".4" stop-color="#c8bfa8"/><stop offset=".7" stop-color="#566f3a"/><stop offset="1" stop-color="#3c5428"/></linearGradient></defs>
      <path d="M0 0H228L125 107 0 231Z" fill="url(#tower)"/>
      <path d="M0 0L125 107 228 0" fill="#fff" opacity="0"/>
      <path d="M38 0L125 104 228 0" fill="none" stroke="#fff" stroke-width="6"/>
      <path d="M40 0L125 100 226 0" fill="none" stroke="var(--navy)" stroke-width="1.8"/>
      <path d="M0 231L115 115" fill="none" stroke="var(--gold)" stroke-width="2"/>
    </svg>
    <div class="title" style="right:24px;top:8px;font-size:25px;text-align:right">YOUR PAGE</div>
    <div class="title" style="right:24px;top:36px;font-size:25px;text-align:right">TITTLE</div>
    <div class="rule" style="left:231px;top:51px;width:63px"></div>
    <svg width="240" height="140" viewBox="0 0 240 140" style="left:62px;top:73px" fill="none" stroke="var(--navy)" stroke-width=".8">
      <g id="tickRing"><circle cx="3.5" cy="3.5" r="3"/><path d="M2 3.6l1.3 1.3 2.7-2.8"/></g>
      <use href="#tickRing" x="107"/><use href="#tickRing" x="73" y="37"/><use href="#tickRing" x="37" y="76"/><use href="#tickRing" x="7" y="115"/>
    </svg>
    <div class="head" style="left:178px;top:72px;font-size:6.4px;font-weight:700">YOUR SUB HEADING</div>
    <p class="body" style="left:178px;top:84px;width:210px">Lorem ipsum dolor sit amet, consectetur adipiscing elit, sed do eiusmod tempor incididunt ut labore et dolore magna aliqua. Quis ipsum suspendisse ultrices .</p>
    <div class="head" style="left:145px;top:108px;font-size:6.4px;font-weight:700">YOUR SUB HEADING</div>
    <p class="body" style="left:145px;top:121px;width:243px">Lorem ipsum dolor sit amet, consectetur adipiscing elit, sed do eiusmod tempor incididunt ut labore et dolore magna aliqua. Quis ipsum suspendisse ultrices gravida. Risus</p>
    <div class="head" style="left:108px;top:147px;font-size:6.4px;font-weight:700">YOUR SUB HEADING</div>
    <p class="body" style="left:108px;top:160px;width:280px">Lorem ipsum dolor sit amet, consectetur adipiscing elit, sed do eiusmod tempor incididunt ut labore dolore magna aliqua. Quis ipsum suspendisse ultrices gravida. Risus</p>
    <div class="head" style="left:78px;top:186px;font-size:6.4px;font-weight:700">YOUR SUB HEADING</div>
    <p class="body" style="left:78px;top:199px;width:310px">Lorem ipsum dolor sit amet, consectetur adipiscing elit, sed do eiusmod tempor incididunt ut labore et dolore magna aliqua. Quis ipsum suspendisse ultrices gravida. Risus</p>
  </section>

</main>
</body>
</html>
```